Food Hall in San Clemente, CA by the Pacific Ocean that has 15 vendors and 2 bars

We need a web page design that highlights our food hall in San Clemente, CA. The name of the food hall is Bellwick Food Hall. Inside of the food hall there are 15 different vendors and 2 bars. The place has a beautiful patio and it is by Pacific Ocean. Most of the vendors are local to San Clemente area. The highly anticipated location is opening during the summer of 2025. Website should have a dropdown menu for the different vendors that are in the food hall and people should be able to click to their respective business website. The website should also include link to our social media channels and also a link to provide comments and subscribe for the mailing list.
Target Market(s)
Mostly residents in the San Clemente, CA and surrounding areas. Couples, families and tourist alike that are looking for an exceptional dining experience that everyone can find something they like.
Industry/Entity Type
Restaurants
Coding
Coded - Design and coding required
Number of Pages Required
5+ page
Font styles to use
Look and feel

```html
<!DOCTYPE html>
<html lang="en">
<head>
<meta charset="UTF-8">
<title>Food and Beverage - Bellwick Food Hall</title>
<link rel="stylesheet" href="https://fonts.googleapis.com/css2?family=Lato:wght@400;700;900&display=swap">
<style>
  :root {
    --sky: #0095d5;
    --navy: #003366;
    --ocean: #0055a8;
    --white: #ffffff;
    --ink: #222222;
  }
  * { margin: 0; padding: 0; box-sizing: border-box; }
  html, body {
    width: 1200px;
    height: 649px;
    overflow: hidden;
    background: var(--ocean);
    font-family: "Lato", sans-serif;
    color: var(--white);
  }
  .site-header {
    height: 92px;
    background: var(--sky);
    position: relative;
  }
  .vendor-title {
    position: absolute;
    top: 13px;
    width: 100%;
    text-align: center;
    font-size: 15px;
    font-weight: 700;
  }
  .brand {
    position: absolute;
    left: 10px;
    top: 55px;
    font-size: 21px;
    font-weight: 900;
  }
  .main-nav {
    position: absolute;
    top: 61px;
    right: 0;
    display: flex;
  }
  .main-nav a {
    width: 86px;
    text-align: center;
    color: var(--white);
    text-decoration: none;
    font-size: 11px;
    font-weight: 700;
  }
  .hero {
    height: 232px;
    background: var(--navy);
    display: flex;
    align-items: center;
    justify-content: center;
    font-size: 15px;
  }
  .content {
    height: 233px;
    padding-top: 21px;
  }
  .menu-card {
    width: 987px;
    height: 180px;
    margin: 0 auto;
    background: var(--white);
    border-radius: 7px;
    padding: 62px 20px 0;
    color: var(--ink);
  }
  .menu-card h2 {
    color: var(--ocean);
    font-size: 21px;
    font-weight: 900;
    margin-bottom: 16px;
  }
  .menu-card p {
    font-size: 11px;
  }
  .site-footer {
    height: 69px;
    background: var(--sky);
    display: flex;
    align-items: center;
    justify-content: center;
    font-size: 11px;
  }
</style>
</head>
<body>
  <header class="site-header">
    <h1 class="vendor-title">Food and Beverage</h1>
    <div class="brand">Bellwick Food Hall</div>
    <nav class="main-nav">
      <a href="#">Home</a>
      <a href="#">Vendors</a>
      <a href="#">About</a>
      <a href="#">Contact</a>
    </nav>
  </header>
  <section class="hero">
    <p>Serving up delicious meals and refreshing drinks to satisfy all tastes</p>
  </section>
  <main class="content">
    <article class="menu-card">
      <h2>Our Menu</h2>
      <p>From gourmet street food to craft beverages, Food and Beverage delivers a unique dining experience. Come taste the innovation and freshness we bring to the table.</p>
    </article>
  </main>
  <footer class="site-footer">
    <p>&copy; 2025 Bellwick Food Hall</p>
  </footer>
</body>
</html>
```